Infectious Diseases Research Laboratory Needs Business Card

We need a business card for an academic research laboratory based in Kansas City called VELKOR. The full lab name is Microbe Exposure Kinetics/Response Modeling Integrated Study Laboratory, but this does not need to be incorporated. We study novel ways to optimize the treatment of multidrug-resistant bacterial infections ("superbugs") throughout the entire biomedical research spectrum (from benchtop to bedside). The name VELKOR is not only an acronym for our lab name, but also represents our desire to make discoveries and explore the unknown (the stars, if you well). It also serves as an ode to the state of Kansas motto where we are based, ad astra per aspera ("to the stars, through difficulty").

Target Market(s)

Pharmaceutical companies, researchers

Industry/Entity Type

Pharmaceutical

Contact Information for Business Card

The business card should incorporate and complement our new logo (see uploaded files). Double-sided designs are preferred. Looking for something modern, but professional.

Font styles to use
Sans Serif

Requirements
Must have
• Double-sided. One side would ideally be a solid color incorporating logo and the other should also have the logo (smaller), but incorporate staff information.
• Color codes:
• Red: #F04C51
• Blue: #3477B5
• Gray: #808285

```html
<!DOCTYPE html>
<html lang="en">
<head>
<meta charset="utf-8">
<title>VELKOR Business Card</title>
<link href="https://fonts.googleapis.com/css2?family=Roboto:wght@400;500;700&display=swap" rel="stylesheet">
<style>
  :root {
    --red: #F04C51;
    --blue: #2F6FAE;
    --white: #F4F4F4;
    --ink-light: #FFFFFF;
    --backdrop: #262626;
    --card-shadow: rgba(0,0,0,0.55);
  }
  * { margin: 0; padding: 0; box-sizing: border-box; }
  html, body {
    width: 1200px; height: 960px; overflow: hidden;
    background: var(--backdrop);
    font-family: "Roboto", sans-serif;
  }
  .card {
    position: absolute;
    width: 600px; height: 342px;
    overflow: hidden;
    box-shadow: 0 3px 6px var(--card-shadow);
  }
  .card-front { left: 314px; top: 113px; background: var(--white); }
  .card-back { left: 311px; top: 472px; background: var(--blue); }

  .front-shapes { position: absolute; inset: 0; }

  .brand {
    position: absolute;
    display: flex; align-items: center; gap: 12px;
  }
  .brand-dot { border-radius: 50%; flex: none; }
  .brand-name { font-weight: 500; letter-spacing: 3px; line-height: 1; }

  .front-brand { left: 49px; top: 47px; }
  .front-brand .brand-dot { width: 58px; height: 58px; background: var(--red); }
  .front-brand .brand-name { font-size: 52px; color: var(--red); }

  .staff {
    position: absolute; right: 24px; top: 166px;
    text-align: right; color: var(--ink-light);
  }
  .staff-name { font-size: 20px; font-weight: 700; line-height: 24px; }
  .staff-title { font-size: 14px; font-weight: 500; line-height: 24px; letter-spacing: 0.3px; }

  .contact-list {
    position: absolute; right: 26px; top: 226px;
    list-style: none; color: var(--ink-light);
    font-size: 14px; line-height: 19px; text-align: right;
  }
  .contact-list li { display: flex; justify-content: flex-end; align-items: center; gap: 8px; }
  .contact-list svg { width: 13px; height: 13px; flex: none; }

  .address {
    position: absolute; right: 235px; top: 284px;
    color: var(--ink-light); font-size: 14px; line-height: 19px; text-align: right;
  }
  .divider {
    position: absolute; left: 383px; top: 284px;
    width: 1px; height: 34px; background: var(--ink-light);
  }

  .back-brand { left: 134px; top: 134px; gap: 14px; }
  .back-brand .brand-dot { width: 66px; height: 66px; background: var(--ink-light); }
  .back-brand .brand-name { font-size: 58px; color: var(--ink-light); }

  .back-web {
    position: absolute; left: 0; right: 0; top: 285px;
    text-align: center; color: var(--ink-light);
    font-size: 14px; letter-spacing: 4px;
  }
</style>
</head>
<body>

<section class="card card-front">
  <svg class="front-shapes" width="600" height="342" viewBox="0 0 600 342" aria-hidden="true">
    <polygon points="600,70 600,342 0,342" fill="var(--blue)"/>
    <polygon points="0,236 102,296 0,342" fill="var(--red)"/>
  </svg>

  <div class="brand front-brand">
    <span class="brand-dot"></span>
    <span class="brand-name">VELKOR</span>
  </div>

  <div class="staff">
    <div class="staff-name">MARA ELLISON</div>
    <div class="staff-title">CEO/FOUNDER</div>
  </div>

  <div class="address">
    2140 Orchard Bend<br>
    Kansas City, Kansas 66160
  </div>
  <span class="divider"></span>

  <ul class="contact-list">
    <li>816 555 0142
      <svg viewBox="0 0 16 16" fill="#fff"><path d="M3 1l3 3-1.5 2c1 2 2.5 3.5 4.5 4.5L11 9l3 3-2 2.5C6 14 2 10 1.5 3z"/></svg>
    </li>
    <li>816 555 0187
      <svg viewBox="0 0 16 16" fill="none" stroke="#fff" stroke-width="1.6"><rect x="4" y="1" width="8" height="14" rx="1.5"/><line x1="7" y1="12.5" x2="9" y2="12.5"/></svg>
    </li>
    <li>816 555 0193
      <svg viewBox="0 0 16 16" fill="#fff"><rect x="4" y="1" width="8" height="5"/><rect x="1" y="6" width="14" height="6" rx="1"/><rect x="4" y="10" width="8" height="5" fill="#2F6FAE" stroke="#fff" stroke-width="1.2"/></svg>
    </li>
    <li>mara@velkorlab.org
      <svg viewBox="0 0 16 16" fill="#fff"><path d="M1 3h14v10H1z"/><path d="M1 3l7 6 7-6" fill="none" stroke="#2F6FAE" stroke-width="1.3"/></svg>
    </li>
    <li>www.velkorlab.org
      <svg viewBox="0 0 16 16"><circle cx="8" cy="8" r="7" fill="#fff"/><path d="M4 5c2 0 2 2 4 2s1 3 0 4M10 3c0 2 2 2 3 3" fill="none" stroke="#2F6FAE" stroke-width="1.3"/></svg>
    </li>
  </ul>
</section>

<section class="card card-back">
  <div class="brand back-brand">
    <span class="brand-dot"></span>
    <span class="brand-name">VELKOR</span>
  </div>
  <div class="back-web">www.velkorlab.org</div>
</section>

</body>
</html>
```